Wildlife photographer Website

The website is to be a "resume" of pictures and awards won by Nora. Lean heavy to outdoor wildlife.
She will post articles and have ability to interact with fans.

I will add some of her pictures tonight,

Target Market(s)

Terra Quarterly .....anyone looking to hire a wildlife photographer.

Industry/Entity Type

Professional Photography

Contact Information for Business Card

Nora Falkett
4817 Maple Hollow Lane
Columbia MD 21078
443-581-2094
Nora@FernOwlPix.com

Coding

Coded - Design and coding required

Number of Pages Required

5+ page

Requirements
Must have
• New Logo
Nice to have
• Nature, and eye catching graphics

```html
<!DOCTYPE html>
<html lang="en">
<head>
<meta charset="utf-8">
<title>Wildlife Photography by Nora</title>
<link href="https://fonts.googleapis.com/css2?family=Poppins:wght@300;400;500;600;700&display=swap" rel="stylesheet">
<style>
:root{
  --ink:#2b2b2b;
  --muted:#6b6b6b;
  --brown:#6b4a2b;
  --gold:#f2c230;
  --white:#ffffff;
  --paper:#ffffff;
  --night:#0d0d0d;
  --forest:#1c2416;
  --line:#d9d9d9;
}
*{box-sizing:border-box;margin:0;padding:0}
html,body{width:1200px;height:2764px;overflow:hidden;background:var(--paper);font-family:'Poppins',sans-serif;color:var(--ink)}
.page{position:relative;width:1200px;height:2764px}
.photo{position:absolute;display:block}
.site-header{position:absolute;left:0;top:0;width:1200px;height:128px}
.brand{position:absolute;left:160px;top:44px;display:flex;align-items:center;gap:10px;font-weight:600;font-size:24px;color:var(--brown)}
.brand-dot{width:18px;height:18px;border-radius:50%;background:var(--brown)}
.main-nav{position:absolute;left:420px;top:48px;display:flex;gap:36px;font-size:14px;font-weight:500;letter-spacing:1px}
.main-nav a{color:var(--ink);text-decoration:none;padding-bottom:6px}
.main-nav a.active{color:var(--gold);border-bottom:2px solid var(--gold)}
.header-social{position:absolute;right:160px;top:50px;display:flex;gap:22px}
.header-social span{width:14px;height:14px;border-radius:50%;border:1.5px solid #999}
.hero-side{top:128px;width:320px;height:392px;background:linear-gradient(180deg,#b9c6cf 0%,#d9cdb6 55%,#eef1f3 100%)}
.hero-side.left{left:0}.hero-side.right{right:0}
.hero-center{left:320px;top:100px;width:560px;height:400px;background:linear-gradient(180deg,#2f3a2a,#4d5a3c 60%,#2b3324);box-shadow:0 10px 30px rgba(0,0,0,.35)}
.hero-text{position:absolute;left:320px;top:220px;width:560px;text-align:center;color:var(--white)}
.hero-text h1{font-size:30px;font-weight:700;color:var(--gold);line-height:1.25;letter-spacing:1px}
.hero-text p{font-size:14px;margin-top:14px;line-height:1.6;padding:0 60px}
.about{position:absolute;left:160px;top:545px;width:360px}
.about h2{font-size:40px;font-weight:600;color:var(--brown);letter-spacing:1px;border-bottom:3px solid var(--brown);display:inline-block;padding-bottom:2px}
.about .lead{font-size:25px;font-weight:300;color:var(--muted);line-height:1.35;margin-top:22px}
.about .body{font-size:12px;color:var(--muted);line-height:1.7;margin-top:22px}
.btn{display:inline-block;margin-top:26px;border:1.5px solid var(--ink);padding:8px 20px;font-size:12px;font-weight:500;letter-spacing:1px}
.about-photo{left:680px;top:540px;width:300px;height:400px;background:linear-gradient(180deg,#7e98b4 0%,#6f8a62 45%,#9c6b4b 100%)}
.news-band{left:0;top:980px;width:1200px;height:340px;background:linear-gradient(90deg,#14190f,#2a3520 50%,#131810)}
.news{position:absolute;left:200px;top:1060px;width:800px;text-align:center;color:var(--white)}
.news h2{font-size:30px;font-weight:600;line-height:1.3}
.news p{font-size:13px;line-height:1.6;margin-top:16px;color:#dcdcdc}
.section-title{position:absolute;left:0;width:1200px;text-align:center}
.section-title h2{font-size:32px;font-weight:600;letter-spacing:1px}
.section-title p{font-size:22px;font-weight:300;color:var(--muted);margin-top:-4px}
.tile{box-shadow:0 2px 6px rgba(0,0,0,.15)}
.watch-card{width:290px;height:220px}
.watch-card span{position:absolute;left:12px;bottom:10px;color:var(--white);font-size:12px}
.site-footer{position:absolute;left:0;top:2420px;width:1200px;height:344px;background:var(--night);color:#cfcfcf}
.fb-box{position:absolute;left:240px;top:60px;width:240px;height:150px;background:#f3f3f3;padding:10px}
.fb-box .thumb{width:40px;height:40px;background:#7c8f6a;display:inline-block;vertical-align:top}
.fb-box b{font-size:12px;color:#333;font-weight:600;margin-left:8px}
.fb-box .cover{margin-top:10px;height:60px;background:linear-gradient(90deg,#8aa07a,#c9b58a)}
.footer-head{position:absolute;left:520px;top:56px;font-size:14px;font-weight:600;color:var(--white);letter-spacing:1px}
.footer-col{position:absolute;top:92px;font-size:12px;line-height:1.75}
.footer-col h4{font-size:13px;color:var(--white);font-weight:600;margin-bottom:4px}
.footer-social{position:absolute;left:456px;top:262px;display:flex;gap:14px}
.footer-social span{width:28px;height:28px;border-radius:50%;background:#555}
.copyright{position:absolute;left:0;bottom:18px;width:1200px;text-align:center;font-size:11px;color:#999}
</style>
</head>
<body>
<div class="page">
  <header class="site-header">
    <div class="brand"><span class="brand-dot"></span>Fern Owl</div>
    <nav class="main-nav">
      <a class="active">HOME</a><a>ABOUT ME</a><a>GALLERY</a><a>CONTACT US</a>
    </nav>
    <div class="header-social"><span></span><span></span><span></span></div>
  </header>

  <div class="photo hero-side left" role="img" aria-label="Hare leaping across snow"></div>
  <div class="photo hero-side right" role="img" aria-label="Hare leaping across snow"></div>
  <div class="photo hero-center" role="img" aria-label="Photographer standing by a lake at dusk"></div>
  <div class="hero-text">
    <h1>THE BEST OF THE WILDLIFE<br>PHOTOGRAPHY</h1>
    <p>Striking images from nature's quiet corners, a wildlife photographer's compilations of the past</p>
  </div>

  <section class="about">
    <h2>ABOUT ME</h2>
    <p class="lead">I've been working as a professional wedding photographer all my adult life.</p>
    <p class="body">My name is Nora and I have been a professional wedding photographer since 2005. On this website you can take a look at my latest photos or order a photo session for yourself or your family.</p>
    <span class="btn">READ MORE</span>
  </section>
  <div class="photo about-photo" role="img" aria-label="Nora hiking with poles among pine trees"></div>

  <div class="photo news-band" role="img" aria-label="Dark forest background"></div>
  <div class="news">
    <h2>Top scientists demand NSW commit to brumby<br>cull in Kosciuszko national park</h2>
    <p>Lorem ipsum dolor sit amet, consectetur adipiscing elit, sed do eiusmod tempor incididunt ut labore et dolore magna aliqua. Ut enim ad minim veniam, quis nostrud exercitation ullamco laboris nisi ut aliquip ex ea commodo consequat duis aute irure.</p>
  </div>

  <div class="section-title" style="top:1350px"><h2>OUR PORTFOLIO</h2><p>Professional Photography</p></div>
  <div class="photo tile" style="left:0;top:1440px;width:288px;height:208px;background:linear-gradient(180deg,#b7c4cf,#e7e2d8)" role="img" aria-label="Hare running in snow"></div>
  <div class="photo tile" style="left:0;top:1664px;width:288px;height:216px;background:linear-gradient(180deg,#3c4a3e,#6b5a44)" role="img" aria-label="Otter in water"></div>
  <div class="photo tile" style="left:308px;top:1440px;width:284px;height:440px;background:linear-gradient(180deg,#6e8a54,#4a6a3a 60%,#8a7a5a)" role="img" aria-label="Hiker on a forest trail"></div>
  <div class="photo tile" style="left:612px;top:1440px;width:288px;height:208px;background:linear-gradient(180deg,#3f5f7c,#2c4a66)" role="img" aria-label="Ducks on blue water"></div>
  <div class="photo tile" style="left:612px;top:1664px;width:288px;height:216px;background:linear-gradient(180deg,#6b4a2a,#c06a2a 60%,#5a3a20)" role="img" aria-label="Red fox in autumn leaves"></div>
  <div class="photo tile" style="left:916px;top:1440px;width:284px;height:440px;background:linear-gradient(180deg,#e6e6e6,#cbbfa6 70%,#b3a183)" role="img" aria-label="Sandpiper on the beach"></div>

  <div class="section-title" style="top:1930px"><h2 style="font-size:28px">WILDLIFE PHOTOGRAPHERS TO WATCH</h2></div>
  <div class="photo watch-card" style="left:292px;top:1990px;height:220px;background:linear-gradient(180deg,#9a8a6a,#4d5a63)" role="img" aria-label="Bird over a golden shoreline"><span>Shoreline</span></div>
  <div class="photo watch-card" style="left:608px;top:1990px;height:220px;background:linear-gradient(180deg,#b8c8d4,#6f7d6a)" role="img" aria-label="Flock of geese in flight"><span>In flight</span></div>
  <div class="photo watch-card" style="left:292px;top:2230px;height:140px;background:linear-gradient(180deg,#d98a3a,#6a4a3a 70%,#3a3a3a)" role="img" aria-label="Sunset over a country road"><span>Open road</span></div>
  <div class="photo watch-card" style="left:608px;top:2230px;height:140px;background:linear-gradient(180deg,#3e5a3a,#6a7a4a)" role="img" aria-label="Photographer in a kayak"><span>On the water</span></div>

  <footer class="site-footer">
    <div class="fb-box"><span class="thumb"></span><b>Fern Owl Pictures</b><div class="cover" role="img" aria-label="Page cover photo"></div></div>
    <div class="footer-head">PHOTOGRAPHY BY NORA</div>
    <div class="footer-col" style="left:520px"><h4>Links</h4>» Get in Touch<br>» About<br>» Blog<br>» Weddings<br>» Print Lovers<br>» Print Gallery</div>
    <div class="footer-col" style="left:680px"><h4>More</h4>» Weddings<br>» Champions<br>» Events<br>» Nature<br>» Email<br>» FAQ</div>
    <div class="footer-col" style="left:840px"><h4>Contact Us</h4>Nora Falkett<br>4817 Maple Hollow Lane<br>Columbia MD 21078<br><br>443-581-2094<br>Nora@FernOwlPix.com</div>
    <div class="footer-social"><span></span><span></span><span></span><span></span><span></span><span></span></div>
    <div class="copyright">© Copyright Photographer 2024. Made by Nora</div>
  </footer>
</div>
</body>
</html>
```